Simple Webpage for Company that offer IT Security Services

Company Type: Penetration Tests, IT Security Services, Security Audits
Company Name: NetBastion
Navigation Style: similar to https://www.veltrapro.com/en/ with Top Navigation (and submenu's)
Top Navigation Items: Services, About Us, Contact
Industry/Entity Type
It Company
Coding
Coded - Design and coding required

```html
<!DOCTYPE html>
<html lang="en">
<head>
<meta charset="utf-8">
<title>NetBastion – IT Security Services</title>
<link href="https://fonts.googleapis.com/css2?family=Roboto:wght@400;500;700&family=Open+Sans:ital,wght@0,400;0,700;1,400;1,700&display=swap" rel="stylesheet">
<style>
  :root{
    --blue:#0a86e0;
    --blue-bright:#1e9cf0;
    --blue-card:#0b8ae6;
    --blue-card-mid:#0a7fd4;
    --ink:#333333;
    --text:#444444;
    --white:#ffffff;
    --dark-band:#1a1d22;
    --charcoal:#3a3a3a;
    --footer:#222222;
    --line:#cfcfcf;
    --muted:#999999;
  }
  *{margin:0;padding:0;box-sizing:border-box}
  html,body{width:1200px;height:3130px;overflow:hidden;background:var(--white)}
  body{position:relative;font-family:"Roboto",Arial,sans-serif;color:var(--text)}
  .abs{position:absolute}

  /* header */
  .site-header{position:absolute;left:0;top:0;width:1200px;height:105px;background:var(--white)}
  .brand{position:absolute;left:46px;top:27px;display:flex;align-items:center;gap:12px}
  .brand-mark{width:44px;height:44px;background:var(--blue);border-radius:50%}
  .brand-name{font-size:40px;font-weight:700;color:var(--blue);letter-spacing:-.5px}
  .topbar{position:absolute;left:730px;top:0;width:470px;height:40px}
  .topbar-info{position:absolute;left:800px;top:0;height:40px;display:flex;align-items:center;gap:40px;color:var(--white);font-size:16px}
  .topbar-info span{display:flex;align-items:center;gap:9px}
  .main-nav{position:absolute;top:64px;left:0;width:1200px}
  .main-nav a{position:absolute;font-size:17px;color:var(--ink);text-decoration:none}
  .main-nav .active::after{content:"";position:absolute;left:-8px;right:-8px;top:34px;height:4px;background:var(--blue)}

  /* hero */
  .hero{position:absolute;left:0;top:105px;width:1200px;height:595px;
    background:linear-gradient(180deg,#5d6a78 0%,#3e4957 45%,#1d242d 100%)}
  .hero-line1{position:absolute;top:206px;width:100%;text-align:center;color:var(--white);font-size:38px;letter-spacing:4px}
  .hero-line2{position:absolute;top:252px;width:100%;text-align:center;color:var(--white);font-size:50px;font-weight:700}
  .btn{position:absolute;display:flex;align-items:center;justify-content:center;font-size:16px;color:var(--white)}
  .btn-hero{left:511px;top:333px;width:178px;height:52px;background:var(--blue)}

  /* section heads */
  .section-title{position:absolute;width:100%;text-align:center;font-size:46px;color:var(--ink);font-weight:400}
  .divider{position:absolute;left:516px;width:168px;height:20px}
  .services-intro{position:absolute;left:67px;top:826px;width:1070px;text-align:center;font-size:15.5px;line-height:24px;color:var(--text)}

  /* services */
  .service-band{position:absolute;left:0;top:1114px;width:1200px;height:468px;
    background:linear-gradient(180deg,#23272d,#121417)}
  .service-card{position:absolute;top:954px;width:343px;height:357px}
  .service-photo{height:160px}
  .service-body{height:197px;padding:26px 22px 0;text-align:center;color:var(--white)}
  .service-body h3{font-size:21px;font-weight:700;margin-bottom:14px;text-transform:uppercase}
  .service-body p{font-size:15.5px;line-height:23px}
  .grow-title{position:absolute;top:1362px;width:100%;text-align:center;font-size:44px;color:var(--white)}
  .grow-sub{position:absolute;top:1427px;width:100%;text-align:center;font-size:27px;color:var(--white)}
  .btn-contact{left:513px;top:1496px;width:176px;height:50px;background:#4a4b4d;font-weight:700;letter-spacing:.5px}

  /* testimonial */
  .testimonial{position:absolute;left:0;top:1582px;width:1200px;height:446px;background:var(--blue)}
  .arrow{position:absolute;top:192px;width:50px;height:50px;border-radius:50%;background:var(--white)}
  .client-photo{position:absolute;left:146px;top:81px;width:188px;height:365px;
    background:linear-gradient(180deg,#c9dbee,#8fb2d6 60%,#2a2f38)}
  .quote-box{position:absolute;left:472px;top:92px;width:592px;height:288px;background:var(--white)}
  .quote-strip{position:absolute;left:0;top:0;width:50px;height:100%;background:#2e2e2e}
  .quote-notch{position:absolute;left:-20px;top:28px;width:0;height:0;border-top:20px solid transparent;border-bottom:20px solid transparent;border-right:20px solid #2e2e2e}
  .quote-open{position:absolute;left:10px;top:12px;color:var(--white);font:700 60px "Open Sans",Arial,sans-serif}
  .quote-text{position:absolute;left:84px;top:44px;width:480px;font:italic 15.5px/24px "Open Sans",Arial,sans-serif;color:var(--ink)}
  .quote-close{position:absolute;left:428px;top:176px;font:700 36px "Open Sans",Arial,sans-serif;color:var(--ink)}
  .quote-name{position:absolute;left:90px;top:212px;font:italic 700 14.5px "Open Sans",Arial,sans-serif;color:var(--ink);letter-spacing:.5px}
  .quote-role{position:absolute;left:90px;top:236px;font:15px "Open Sans",Arial,sans-serif;color:var(--text)}

  /* contact */
  .call-label{position:absolute;top:2174px;width:100%;text-align:center;font-size:19px;font-weight:700;color:var(--ink)}
  .call-number{position:absolute;top:2202px;width:100%;text-align:center;font-size:46px;font-weight:700;color:var(--blue-bright);letter-spacing:1px}
  .field{position:absolute;height:44px;border:1px solid var(--line);background:var(--white);
    font-size:13px;color:var(--muted);display:flex;align-items:center;justify-content:center}
  .field-message{left:65px;top:2367px;width:1079px;height:146px;align-items:flex-start;justify-content:flex-start;padding:12px}
  .btn-submit{left:434px;top:2542px;width:340px;height:46px;background:var(--blue-bright);font-size:14px;font-weight:700}

  .map{position:absolute;left:0;top:2640px;width:1200px;height:278px;
    background:linear-gradient(90deg,#dde6c9 0%,#e9e4cf 45%,#dfe6cc 75%,#aacdf2 90%)}

  .social{position:absolute;left:0;top:2918px;width:1200px;height:129px;background:var(--charcoal)}
  .social-dot{position:absolute;top:35px;width:62px;height:62px;border-radius:50%;background:#555555}
  .site-footer{position:absolute;left:0;top:3047px;width:1200px;height:83px;background:var(--footer);
    color:#cfcfcf;font-size:14.5px;text-align:center;padding-top:22px;line-height:21px}
</style>
</head>
<body>

<header class="site-header">
  <div class="brand"><span class="brand-mark"></span><span class="brand-name">NetBastion</span></div>
  <svg class="topbar" viewBox="0 0 470 40" width="470" height="40"><polygon points="0,0 470,0 470,40 36,40" fill="#0a86e0"/></svg>
  <div class="topbar-info">
    <span><svg width="15" height="15" viewBox="0 0 24 24"><path fill="#fff" d="M6.6 10.8a15 15 0 0 0 6.6 6.6l2.2-2.2c.3-.3.7-.4 1-.2 1.1.4 2.3.6 3.6.6.6 0 1 .4 1 1V20c0 .6-.4 1-1 1A17 17 0 0 1 3 4c0-.6.4-1 1-1h3.5c.6 0 1 .4 1 1 0 1.3.2 2.5.6 3.6.1.3 0 .7-.2 1z"/></svg>555.204.7731</span>
    <span><svg width="17" height="13" viewBox="0 0 24 18"><rect x="1" y="1" width="22" height="16" fill="none" stroke="#fff" stroke-width="2"/><path d="M1 1l11 9 11-9" fill="none" stroke="#fff" stroke-width="2"/></svg>hello@netbastion.net</span>
  </div>
  <nav class="main-nav">
    <a class="active" style="left:810px">Services</a>
    <a style="left:943px">About Us</a>
    <a style="left:1083px">Contact</a>
  </nav>
</header>

<section class="hero" role="img" aria-label="Upward view of glass office towers against a cloudy sky">
  <div class="hero-line1">We Build Perfect</div>
  <div class="hero-line2">Website For Your Business</div>
  <span class="btn btn-hero">View Our Projects</span>
</section>

<h2 class="section-title" style="top:730px">Our Services</h2>
<svg class="divider" style="top:785px" viewBox="0 0 168 20"><line x1="0" y1="10" x2="68" y2="10" stroke="#0a86e0" stroke-width="2"/><line x1="100" y1="10" x2="168" y2="10" stroke="#0a86e0" stroke-width="2"/><rect x="77" y="3" width="14" height="14" fill="#333"/></svg>
<p class="services-intro">Lorem Ipsum is simply dummy text of the printing and typesetting industry. Lorem Ipsum has been the industry's standard dummy text ever since the 1500s, when an unknown printer took a galley of type and scrambled it to make a type specimen book. It has survived not only five centuries, but also the leap into electronic typesetting, remaining essentially unchanged.</p>

<section class="service-band" role="img" aria-label="Dim server room with a person standing between racks">
  <h2 class="grow-title" style="top:248px">We Can Help You To Grow Up Your Online Business</h2>
  <p class="grow-sub" style="top:313px">We Offer A Wide Range Of Procedures To Help You Get The Perfect Smile</p>
  <span class="btn btn-contact" style="top:382px">CONTACT US</span>
</section>

<article class="service-card" style="left:88px">
  <div class="service-photo" role="img" aria-label="Technician inspecting a laptop" style="background:linear-gradient(135deg,#e6ebef,#9aa6b0)"></div>
  <div class="service-body" style="background:var(--blue-card)"><h3>Penetration Tests</h3><p>Lorem Ipsum is simply dummy text of the printing and typesetting industry. Lorem Ipsum has been the industry's standard dummy text ever since the</p></div>
</article>
<article class="service-card" style="left:431px">
  <div class="service-photo" role="img" aria-label="Analyst working at glowing monitors" style="background:linear-gradient(135deg,#2f6fb8,#0b1a33)"></div>
  <div class="service-body" style="background:var(--blue-card-mid)"><h3>IT Security Services</h3><p>Lorem Ipsum is simply dummy text of the printing and typesetting industry. Lorem Ipsum has been the industry's standard dummy text ever since the</p></div>
</article>
<article class="service-card" style="left:774px">
  <div class="service-photo" role="img" aria-label="Padlock resting on a laptop keyboard" style="background:linear-gradient(135deg,#c3c9d0,#3d434b)"></div>
  <div class="service-body" style="background:var(--blue-card)"><h3>Security Audits</h3><p>Lorem Ipsum is simply dummy text of the printing and typesetting industry. Lorem Ipsum has been the industry's standard dummy text ever since the</p></div>
</article>

<section class="testimonial">
  <svg class="arrow" style="left:46px" viewBox="0 0 50 50"><circle cx="25" cy="25" r="25" fill="#fff"/><path d="M29 15L19 25l10 10" fill="none" stroke="#333" stroke-width="4"/></svg>
  <svg class="arrow" style="left:1104px" viewBox="0 0 50 50"><circle cx="25" cy="25" r="25" fill="#fff"/><path d="M21 15l10 10-10 10" fill="none" stroke="#333" stroke-width="4"/></svg>
  <div class="client-photo" role="img" aria-label="Smiling client in a light blue shirt holding a laptop"></div>
  <blockquote class="quote-box">
    <div class="quote-notch"></div>
    <div class="quote-strip"><span class="quote-open">&ldquo;</span></div>
    <p class="quote-text">Lorem Ipsum is simply dummy text of the printing and typesetting industry. Lorem Ipsum has been the industry's standard dummy text ever since the 1500s, when an unknown printer took a galley of type and scrambled it to make a type specimen book. It has survived not only five centuries, but also the leap into electronic typesetting, remaining essentially unchanged.</p>
    <span class="quote-close">&rdquo;</span>
    <p class="quote-name">MARCUS WHITFIELD</p>
    <p class="quote-role">Software engineer at Halcyon Works | Riverton, Ontario</p>
  </blockquote>
</section>

<h2 class="section-title" style="top:2057px">Contact Form</h2>
<svg class="divider" style="top:2123px" viewBox="0 0 168 20"><line x1="0" y1="10" x2="68" y2="10" stroke="#0a86e0" stroke-width="2"/><line x1="100" y1="10" x2="168" y2="10" stroke="#0a86e0" stroke-width="2"/><rect x="77" y="3" width="14" height="14" fill="#333"/></svg>
<p class="call-label">NEED HELP? CALL US</p>
<p class="call-number">+800 555019284</p>

<form>
  <div class="field" style="left:65px;top:2294px;width:342px">Name</div>
  <div class="field" style="left:434px;top:2294px;width:340px">Email</div>
  <div class="field" style="left:804px;top:2294px;width:340px">Phone</div>
  <div class="field field-message">Message</div>
  <span class="btn btn-submit">Submit</span>
</form>

<div class="map" role="img" aria-label="Road map of London and the surrounding south-east with a location pin"></div>

<section class="social">
  <span class="social-dot" style="left:257px"></span>
  <span class="social-dot" style="left:334px"></span>
  <span class="social-dot" style="left:409px"></span>
  <span class="social-dot" style="left:484px"></span>
  <span class="social-dot" style="left:560px"></span>
  <span class="social-dot" style="left:635px"></span>
  <span class="social-dot" style="left:710px"></span>
  <span class="social-dot" style="left:787px"></span>
</section>

<footer class="site-footer">All Rights Reserved Design by my company<br>&copy;2017 NetBastion</footer>

</body>
</html>
```